Stationery Design Project

Brisk-Span Consultants is interim management company. We are specialized in finding the best Finance and IT consultants for our clients when they require additional resources on an interim basis for projects or special situations. We are flexible in our approach and we always seek to maximize the benefits for our clients as well as our consultants.

We are looking for a design of our letterhead, general stationery and business cards using the company name. The design will also be found on our coming web pages.
Updates

Please also create a logo for Brisk-Span Consultants which expresses that we want to match the best finance and IT people to our customers projects

Target Market(s)

Larger and mid sized companies (all sectors), as well as highly skilled Finance & IT professionals/consultants

Industry/Entity Type

Business

Requirements
Must have
• Brisk-Span Consultants
We are expecting that 'Brisk-Span' will be on the first line and 'Consultants' on a second line.
Please also indicate style of the letters for our address/phone and mail details. Our current address is:
Tornagervej 14,
2915 Skovlunde
Danmark
Mobile: +45 XX XX XX XX Mail: xx@brisk-span.dk

```html
<!DOCTYPE html>
<html lang="en">
<head>
<meta charset="utf-8">
<title>Brisk-Span Consultants – Stationery</title>
<link rel="stylesheet" href="https://fonts.googleapis.com/css2?family=Open+Sans:wght@300;400;700&display=swap">
<style>
  :root {
    --brand-blue: #0a7dcc;
    --brand-grey: #8f8f8a;
    --text-dark: #2b2b2b;
    --text-muted: #8a8a8a;
    --paper: #ffffff;
    --page-bg: #ffffff;
    --sig-tone: #d9d9d9;
  }
  * { box-sizing: border-box; margin: 0; padding: 0; }
  html, body { width: 1200px; height: 900px; overflow: hidden; background: var(--page-bg); }
  body { font-family: "Open Sans", Arial, sans-serif; color: var(--text-dark); position: relative; }

  .sheet {
    position: absolute; background: var(--paper); overflow: hidden;
    box-shadow: 2px 6px 14px rgba(0,0,0,0.18);
  }
  .letterhead { left: 99px; top: 50px; width: 564px; height: 796px; border-radius: 62px 0 52px 0; }
  .card-front { left: 704px; top: 50px; width: 271px; height: 165px; border-radius: 32px 0 26px 0; }
  .card-back  { left: 704px; top: 247px; width: 271px; height: 165px; border-radius: 0 32px 0 32px; background: var(--brand-blue); }

  .wordmark { position: absolute; font-weight: 700; color: var(--brand-blue); line-height: 1; }
  .wordmark .mark-square { display: inline-block; background: var(--brand-blue); vertical-align: top; }
  .wordmark .name-line { display: block; }

  .letterhead .wordmark { left: 346px; top: 52px; font-size: 22px; display: flex; gap: 8px; }
  .letterhead .mark-square { width: 34px; height: 34px; }
  .letterhead .name-sub { font-size: 14px; margin-top: 3px; }

  .card-front .wordmark { left: 80px; top: 17px; font-size: 19px; display: flex; gap: 7px; }
  .card-front .mark-square { width: 30px; height: 30px; }
  .card-front .name-sub { font-size: 12px; margin-top: 2px; }

  .card-back .wordmark { left: 0; right: 0; top: 93px; text-align: center; color: #fff; font-size: 18px; }
  .card-back .name-sub { font-size: 11px; margin-top: 2px; }
  .card-back .mark-square { width: 30px; height: 30px; background: #fff; margin-bottom: 8px; position: absolute; left: 121px; top: -50px; }

  .contact { position: absolute; color: var(--text-muted); font-weight: 300; }
  .letterhead .contact { left: 390px; top: 102px; font-size: 10px; line-height: 12.5px; }
  .card-front .contact { left: 121px; top: 70px; font-size: 8.5px; line-height: 10px; }
  .contact .gap { height: 8px; }
  .contact .role { font-style: italic; font-size: 7px; }
  .contact .key { display: inline-block; width: 10px; }

  .letter-body { position: absolute; left: 41px; top: 193px; width: 440px; font-size: 10px; line-height: 12.5px; word-break: break-all; }
  .letter-body p { margin-bottom: 12.5px; }

  .sign-off { position: absolute; left: 41px; top: 645px; font-size: 10px; }
  .signature { position: absolute; left: 24px; top: 680px; width: 160px; height: 30px; background: linear-gradient(90deg, var(--sig-tone), #f2f2f2); border-radius: 4px; }
  .sign-line { position: absolute; left: 41px; top: 709px; width: 144px; border-top: 1px solid var(--text-dark); }
  .sign-name { position: absolute; left: 41px; top: 712px; font-size: 10px; }

  .edge-band { position: absolute; bottom: 0; height: 6px; }
  .letterhead .band-blue { left: 0; width: 344px; background: var(--brand-blue); }
  .letterhead .band-grey { left: 344px; width: 182px; background: var(--brand-grey); }
  .card-front .band-blue { left: 0; width: 121px; background: var(--brand-blue); }
  .card-front .band-grey { left: 121px; width: 150px; background: var(--brand-grey); }

  .label { position: absolute; font-size: 23px; font-weight: 400; color: var(--text-dark); }
  .label-front { left: 998px; top: 193px; }
  .label-back { left: 998px; top: 390px; }
  .label-card { left: 768px; top: 444px; }
  .label-letter { left: 678px; top: 823px; }

  .swatch { position: absolute; top: 785px; width: 88px; height: 88px; }
  .swatch-blue { left: 972px; background: var(--brand-blue); }
  .swatch-grey { left: 1084px; background: var(--brand-grey); }
</style>
</head>
<body>

<section class="sheet letterhead" aria-label="Letterhead">
  <div class="wordmark">
    <span class="mark-square"></span>
    <span><span class="name-line">Brisk-Span</span><span class="name-line name-sub">Consultants</span></span>
  </div>
  <div class="contact">
    <div>Tornagervej 14,</div>
    <div>2915 Skovlunde</div>
    <div>Danmark.</div>
    <div class="gap"></div>
    <div><span class="key">m</span> +45 XX XX XX XX</div>
    <div><span class="key">e</span> xx@brisk-span.dk</div>
  </div>

  <div class="letter-body">
    <p>Dear Sir,</p>
    <p>Sadljhsadljfh alsdhflakjhgladfkhgldjfgldfhglhdgfiofiye[rpiohf[aifh[aiwhfshsdfuhaldkjhgdkjhgakjdfglkjhg;ksuhf lksdjga;kdfh ;ahf ai risafh akshfdbv;hfoiewhfkudhfgkbciubdgfbfhjdn,sdljdkv jsnjsakdfs fsadaskfnsf sff.</p>
    <p>;sdkjnfk snf'sld'ajd'a djasnfksdjfds adks dksad klsjflksjfk jdail dklasfh guhaudh ashf o fl f'lsdjv'kdfhg lisjd gkgihjfgdf'gadfjg 'lag sadljhsadljfh alsdhflakjhgladfkhgldjfgldfhglhdgfiofiye[rpiohf[aifh[aiwhfshsdfuhaldkjhgdkjhgakjdfglkjhg;ksuhf lksdjga;kdfh ;ahf ai risafh akshfdbv;hfoiewhfkudhfgkbciubdgfbfhjdn,sdljdkv jsnjsakdfs fsadaskfnsf sff.</p>
    <p>;sdkjnfk snf'sld'ajd'a djasnfksdjfds adks dksad klsjflksjfk jdail dklasfh guhaudh ashf o fl f'lsdjv'kdfhghgladfkhgldjfgldfhglhdgfiofiyE[RPIOHF[aifh[aiwhfshSDFUHALDKJHGDKJHGAKJDFGLKJHG;ksuhf lksdjga;kdfh ;ahf ai risafh akshfdbv;hfoiewhfkudhfgkbciubdgfbfhjdn,sdljdkv jsnjsakdfs fsadaskfnsf sff</p>
    <p>;sdkjnfk snf'sld'ajd'a djasnfksdjfds adks dksad klsjflksjfk jdail dklasfh guhaudh ashf o fl f'lsdjv'kdfhg</p>
    <p>lisjd gkgihjfgdf'gadfjg 'lag</p>
  </div>

  <div class="sign-off">adhakud ljsadhfl,</div>
  <div class="signature" role="img" aria-label="Handwritten signature of Erik Holm"></div>
  <div class="sign-line"></div>
  <div class="sign-name">Erik Holm</div>

  <div class="edge-band band-blue"></div>
  <div class="edge-band band-grey"></div>
</section>

<section class="sheet card-front" aria-label="Business card front">
  <div class="wordmark">
    <span class="mark-square"></span>
    <span><span class="name-line">Brisk-Span</span><span class="name-line name-sub">Consultants</span></span>
  </div>
  <div class="contact">
    <div>Erik Holm</div>
    <div class="role">Co-Founder</div>
    <div class="gap"></div>
    <div>Tornagervej 14,</div>
    <div>2915 Skovlunde</div>
    <div>Danmark</div>
    <div class="gap" style="height:4px"></div>
    <div><span class="key">m</span> +45 XX XX XX XX</div>
    <div><span class="key">e</span> xx@brisk-span.dk</div>
  </div>
  <div class="edge-band band-blue"></div>
  <div class="edge-band band-grey"></div>
</section>

<section class="sheet card-back" aria-label="Business card back">
  <div class="wordmark">
    <span class="mark-square"></span>
    <span class="name-line">Brisk-Span</span>
    <span class="name-line name-sub">Consultants</span>
  </div>
</section>

<div class="label label-front">Front</div>
<div class="label label-back">Back</div>
<div class="label label-card">Business Card</div>
<div class="label label-letter">Letter Head</div>

<div class="swatch swatch-blue" aria-label="Brand blue"></div>
<div class="swatch swatch-grey" aria-label="Brand grey"></div>

</body>
</html>
```